Flyer Design Project

We need a flyer design for a 1 year old domestic cleaning company based in Wiltshire, England. We provide households with high quality, hard working cleaners. We would like to see designs which use blue (the colour on the logo attatched). The final design should communicate a clean, premier and thorough service in a clear and bold way. We would like the flyer to be A5 with a single sided design. We have attached an A5 word document with the words we would like to be used in the design, what we need is for you to give it some life, colour, artwork and a professional touch. We are perfectionsists which we would like to illustrate to our customer through this flyer.
Updates

payment has been guaranteed!

Sorry..... please no pictures of females on the designs. many thanks

Target Market(s)

females with higher than average income, aged 30-50. Have families and work 9-5.

Industry/Entity Type

It Company

Requirements
Must have
• The flyer must include the logo attatched and the words in the A5 document attatched. With RELIABLE CLEANERS preferably the headline. A5 - single sided.
The Flyer must also include our introductory offer.....
First Clean FREE
Allow us to demonstrate our standards

this should be emphasised.

PLEASE NOTE: can this be added to the list of words on the flyer please:

Ironing service - one day turn around
Nice to have
• some pictures - nothing cheesey. Again, pictures should communicate our modern professional approach.

```html
<!DOCTYPE html>
<html lang="en">
<head>
<meta charset="utf-8">
<title>Brookmere Cleaners – Flyer</title>
<link rel="stylesheet" href="https://fonts.googleapis.com/css2?family=Anton&family=Open+Sans:wght@400;600;700;800&display=swap">
<style>
  :root {
    --brand-blue: #1a4fd8;
    --bright-blue: #1f6fe8;
    --offer-ring: #3cc0f0;
    --offer-core: #1e7fe0;
    --offer-deep: #0d5bc4;
    --ink: #111111;
    --paper-top: #ffffff;
    --paper-bottom: #bfeaf7;
    --white: #ffffff;
  }
  * { box-sizing: border-box; margin: 0; padding: 0; }
  html, body { width: 1200px; height: 846px; overflow: hidden; background: #ffffff; }
  .flyer {
    position: relative;
    width: 1200px;
    height: 846px;
    overflow: hidden;
    font-family: "Open Sans", Arial, sans-serif;
    color: var(--ink);
    background: linear-gradient(160deg, var(--paper-top) 0%, #eef9fd 35%, #d6f2fb 65%, var(--paper-bottom) 100%);
    border: 2px solid #d7eef7;
  }
  .brand {
    position: absolute;
    left: 120px;
    top: 28px;
    display: flex;
    align-items: center;
    gap: 16px;
  }
  .brand-dot {
    width: 58px;
    height: 58px;
    border-radius: 50%;
    background: var(--brand-blue);
  }
  .brand-name {
    font-family: "Open Sans", Arial, sans-serif;
    font-weight: 700;
    font-size: 46px;
    color: var(--brand-blue);
    letter-spacing: -0.5px;
  }
  .brand-tagline {
    position: absolute;
    left: 214px;
    top: 152px;
    font-weight: 700;
    font-size: 22px;
    color: var(--ink);
  }
  .headline {
    position: absolute;
    left: 60px;
    top: 218px;
    font-family: "Anton", Impact, sans-serif;
    font-size: 66px;
    line-height: 1;
    letter-spacing: 0.5px;
    color: var(--ink);
  }
  .services {
    position: absolute;
    left: 54px;
    top: 328px;
    list-style: none;
  }
  .services li {
    position: relative;
    padding-left: 30px;
    font-weight: 700;
    font-size: 27px;
    line-height: 54px;
    color: var(--ink);
  }
  .services li::before {
    content: "";
    position: absolute;
    left: 0;
    top: 21px;
    width: 13px;
    height: 13px;
    border-radius: 50%;
    background: var(--bright-blue);
  }
  .offer {
    position: absolute;
    left: 712px;
    top: -146px;
    width: 500px;
    height: 500px;
  }
  .offer svg { position: absolute; inset: 0; }
  .offer-text {
    position: absolute;
    left: 0;
    right: 0;
    top: 176px;
    text-align: center;
    color: var(--white);
  }
  .offer-lead { font-weight: 600; font-size: 37px; line-height: 44px; }
  .offer-free { font-weight: 800; font-size: 94px; line-height: 96px; letter-spacing: 2px; }
  .offer-note { font-weight: 600; font-size: 25px; line-height: 34px; margin-top: 6px; }
  .phone {
    position: absolute;
    left: 722px;
    top: 378px;
    font-weight: 700;
    font-size: 44px;
    color: var(--bright-blue);
  }
  .supplies-art {
    position: absolute;
    left: 596px;
    top: 466px;
    width: 230px;
    height: 240px;
    border-radius: 40px 40px 60px 60px;
    background: radial-gradient(circle at 50% 40%, #f2f6f8 0%, #c9dbe6 55%, rgba(191,234,247,0) 75%),
                linear-gradient(160deg, #f5d24a 0%, #4a8ee6 45%, #e84a4a 80%);
    opacity: 0.85;
  }
  .sponges-art {
    position: absolute;
    left: 800px;
    top: 452px;
    width: 400px;
    height: 394px;
    border-top-left-radius: 120px;
    background: linear-gradient(135deg, #78d83c 0%, #3a8ef0 30%, #7a3ad8 52%, #f0804a 72%, #5fd03a 100%);
  }
  .email {
    position: absolute;
    left: 96px;
    top: 766px;
    font-size: 25px;
    color: var(--ink);
  }
</style>
</head>
<body>
<main class="flyer">
  <header class="brand">
    <span class="brand-dot"></span>
    <span class="brand-name">Brookmere Cleaners</span>
  </header>
  <p class="brand-tagline">Premier Domestic Cleaners</p>

  <section class="offer">
    <svg viewBox="0 0 500 500" width="500" height="500" aria-hidden="true">
      <defs>
        <radialGradient id="ringGlow" cx="50%" cy="50%" r="50%">
          <stop offset="80%" stop-color="#8fe0fb"/>
          <stop offset="100%" stop-color="#3cc0f0"/>
        </radialGradient>
        <radialGradient id="coreFill" cx="50%" cy="40%" r="60%">
          <stop offset="0%" stop-color="#2f9bf0"/>
          <stop offset="100%" stop-color="#0d5bc4"/>
        </radialGradient>
      </defs>
      <circle cx="250" cy="250" r="222" fill="url(#ringGlow)"/>
      <circle cx="250" cy="250" r="196" fill="var(--white)" opacity="0.55"/>
      <circle cx="250" cy="250" r="184" fill="url(#coreFill)"/>
    </svg>
    <div class="offer-text">
      <p class="offer-lead">First Clean</p>
      <p class="offer-free">FREE</p>
      <p class="offer-note">Allow us to demonstrate<br>our standards...</p>
    </div>
  </section>

  <h1 class="headline">RELIABLE CLEANERS!</h1>

  <ul class="services">
    <li>Personalised Service</li>
    <li>Constantly Thorough</li>
    <li>Hassel Free</li>
    <li>Insured</li>
    <li>Regular Weekly Cleans</li>
    <li>No Contracts</li>
    <li>Ironing Service - One day turn around</li>
  </ul>

  <p class="phone">Tele: 07700900481</p>

  <div class="supplies-art" role="img" aria-label="Bucket of cleaning supplies with spray bottles and rubber gloves"></div>
  <div class="sponges-art" role="img" aria-label="Stack of colourful cleaning sponges in green, blue, purple and orange"></div>

  <p class="email">Email: brookmerecleaners@mailbox.co.uk</p>
</main>
</body>
</html>
```